Postcard Design

I am an attorney and have my own law firm, Law Offices of Marcus T. Hollis. My address is 4825 Brandell Parkway, #512, Glen Burnie, MD 21068. (410) 555-0172. E-mail kpfirm@quillmail.example.

I want to design two full color postcards, I think the size is about 8.5 by 5.5.

The first is attact Driving While Suspended and Driving Without Insurance client's. I have a list of people charged with those crimes and the postcard goes out each week.

I have been sending letters for years and have been successful but am looking to send only postcards. I am very good at writing the message, terrible with art work. I need you to place the information that I provide below onto a post card with the idea that all of those that receive it will call me. Each person charged receives about 5 postcards and 10 letters from lawyers. No other lawyer advertises just Driving While Suspended and Driving Without Insurance, they all advertise DUI/DWI and other types. My goal is for the client to see my postcard and say "I might as well throw the other stuff away because this is the guy who can do my case well for a great price."

Here are the words that I want on the postcard. Some large, some small. Artwork and good coloring a must, that's what I need help with. Need to use both sides and leave only room for address label and stamp.

DRIVING SUSPENDED AND DRIVING WITHOUT INSURANCE $395.00 FLAT FEE.....INCLUDES ALL UNDERLYING CHARGES!

I have have handled over 5000 cases in AA County and Howard County for more than 22 years. I know the Judges, they know me. There is NO reason to spend omre than $395.00 for a first offense driving suspended or driving without insurance. Should you have a lawyer? Yes, nobody should go to court alone. Should you call me? Over 5000 satisfied client's would say so.

MANY CASES DISMISSED BEFORE COURT!

MONEY BACK GUARANTEE......YOU WILL NOT GET POINTS ON YOUR LICENSE FOR YOUR FIRST OFFENSE DRIVING SUSPENDED OR DRIVING WITHOUT INSURANCE. IF YOU DO, I WILL REFUND YOUR ENTIRE FEE!

Law Offices of Marcus T. Hollis

Marcus T. Hollis, Traffic Defense Attorney

FREE CONSULTATION, PHONES ANSWERED 24/7

HARBOR CREST BUILDING
4825 Brandell Parkway, #512
Glen Burnie, MD 21068

(410) 555-0172

APPOINTMENTS AVAILABLE DAY, EVENING AND WEEKENDS

Requirements
Must have
• The ad must also include small language on each side of the postcard that says "this is an advertisement"

```html
<!DOCTYPE html>
<html lang="en">
<head>
<meta charset="utf-8">
<title>Driving Suspended &amp; Driving Without Insurance – Flat Fee Postcard</title>
<link rel="stylesheet" href="https://fonts.googleapis.com/css2?family=Playfair+Display:wght@800;900&family=Tinos:ital,wght@0,400;0,700;1,400&family=Open+Sans:wght@400;700&display=swap">
<style>
  :root {
    --band-orange: #f59b36;
    --band-orange-deep: #f28c28;
    --price-yellow: #ffe36e;
    --price-yellow-soft: #ffd452;
    --cream: #fffac4;
    --guarantee-fill: #ffd560;
    --guarantee-edge: #c4202b;
    --maroon: #861b1e;
    --ink: #1d1d1d;
  }
  * { box-sizing: border-box; margin: 0; padding: 0; }
  html, body { width: 1200px; height: 930px; overflow: hidden; background: var(--cream); }
  .postcard { position: relative; width: 1200px; height: 930px; background: var(--cream); overflow: hidden; }

  .top-band { position: absolute; left: 0; top: 0; width: 1200px; height: 222px;
    background: linear-gradient(90deg, var(--band-orange-deep), var(--band-orange)); }
  .bottom-band { position: absolute; left: 0; top: 888px; width: 1200px; height: 42px; background: var(--band-orange); }

  .headline { position: absolute; left: 42px; top: 30px; color: var(--maroon);
    font-family: "Playfair Display", "Times New Roman", serif; font-weight: 900;
    font-size: 54px; line-height: 60px; transform: scaleX(0.78); transform-origin: left top;
    letter-spacing: 4px; white-space: nowrap; }
  .headline .spread { letter-spacing: 15px; }

  .price-panel { position: absolute; left: 620px; top: 30px; width: 550px; height: 180px;
    background: linear-gradient(90deg, var(--band-orange) 0%, var(--price-yellow-soft) 25%, var(--price-yellow) 100%); }
  .price { position: absolute; left: 38px; top: -2px; color: var(--maroon);
    font-family: "Playfair Display", "Times New Roman", serif; font-weight: 900;
    font-size: 120px; line-height: 140px; transform: scaleX(0.66); transform-origin: left top; white-space: nowrap; }
  .price-label { position: absolute; left: 375px; top: 14px; color: var(--maroon);
    font-family: "Playfair Display", "Times New Roman", serif; font-weight: 900;
    font-size: 62px; line-height: 58px; transform: scaleX(0.88); transform-origin: left top; white-space: nowrap; }
  .price-note { position: absolute; left: 38px; top: 136px; color: var(--maroon);
    font-family: "Open Sans", Arial, sans-serif; font-size: 22px; white-space: nowrap; }

  .pitch { position: absolute; left: 42px; top: 250px; width: 546px; color: var(--ink);
    font-family: "Tinos", "Times New Roman", serif; font-size: 32px; line-height: 43.5px; text-align: justify; }
  .pitch p + p { margin-top: 13px; }
  .pitch em { font-style: italic; }

  .dismissed { position: absolute; left: 42px; top: 748px; color: var(--ink);
    font-family: "Tinos", "Times New Roman", serif; font-weight: 700; font-size: 32px; line-height: 40px; white-space: nowrap; }
  .firm-name { position: absolute; left: 42px; top: 838px; color: var(--ink);
    font-family: "Tinos", "Times New Roman", serif; font-size: 25px; white-space: nowrap; }
  .ad-notice { position: absolute; left: 44px; top: 882px; z-index: 2; color: var(--ink);
    font-family: Arial, Helvetica, sans-serif; font-size: 15px; line-height: 18px; white-space: nowrap; }

  .guarantee { position: absolute; left: 655px; top: 268px; width: 492px; height: 382px;
    border: 2.5px solid var(--guarantee-edge); border-radius: 20px;
    background: linear-gradient(180deg, #ffdc6a, var(--guarantee-fill)); }
  .guarantee-title { position: absolute; left: 91px; top: 14px; color: #111;
    font-family: "Open Sans", Arial, sans-serif; font-weight: 700; font-size: 43px; line-height: 58px; white-space: nowrap; }
  .guarantee-text { position: absolute; left: 16px; top: 141px; width: 457px; color: var(--ink);
    font-family: "Tinos", "Times New Roman", serif; font-size: 32.5px; line-height: 44.5px; text-align: justify; }

  .consult { position: absolute; left: 657px; top: 665px; color: var(--maroon);
    font-family: "Tinos", "Times New Roman", serif; font-weight: 700; font-size: 41px; line-height: 50px; white-space: nowrap; }
  .contact { position: absolute; left: 659px; top: 764px; color: var(--ink); font-style: normal;
    font-family: "Open Sans", Arial, sans-serif; font-size: 22px; line-height: 32px; white-space: nowrap; }
</style>
</head>
<body>
<main class="postcard">
  <div class="top-band"></div>
  <div class="bottom-band"></div>

  <h1 class="headline">DRIVING SUSPENDED &amp;<br>DRIVING WITHOUT<br><span class="spread">INSURANCE</span></h1>

  <div class="price-panel">
    <div class="price">$395.00</div>
    <div class="price-label">FLAT<br>FEE..</div>
    <div class="price-note">Includes all underlying charges!</div>
  </div>

  <section class="pitch">
    <p>I have have handled over 5000 cases in AA County and Howard County for more than 22 years. I know the Judges, they know me. There is NO reason to spend more than $395.00 for a first offense driving suspended or driving without insurance.</p>
    <p>Should you have a lawyer? Yes, nobody should go to court alone. Should you call me? <em>Over 5000 satis-<br>fied client's would say so.</em></p>
  </section>

  <p class="dismissed">MANY CASES DISMISSED<br>BEFORE COURT!</p>
  <p class="firm-name">Law Offices of Marcus T. Hollis</p>
  <p class="ad-notice">This is an advertisement</p>

  <aside class="guarantee">
    <h2 class="guarantee-title">MONEY BACK<br>GUARANTEE...</h2>
    <p class="guarantee-text">You will not get points on your license for your first offense driving suspended or driving without insurance. If you do, I will refund your entire fee!</p>
  </aside>

  <p class="consult">FREE CONSULTATION,<br>PHONES ANSWERED 24/7</p>
  <address class="contact">
    Marcus T. Hollis, Traffic Defense Attorney<br>
    HARBOR CREST BUILDING<br>
    4825 Brandell Parkway, &nbsp;#512<br>
    Glen Burnie, MD 21068, &nbsp;(410) 555-0172
  </address>
</main>
</body>
</html>
```